Swimming Pool Service business card needed!!!! Please

Hi Everyone! Thanks for looking at my contest. I PROMISE to provide excellent feedback during this process.

I am starting a new swimming pool cleaning business in San Diego, California and would like your help in making a business card for me.

I like easy to read, classy and sophisticated.

I am having a website designed and I'm looking for it to have pictures of really clean & clear pools.

I really like the blue on white color format, but open to other colors.

I do not have a logo, but the name of my company is GLIMMERTIDE POOL SERVICE.

My tag line is: Pools so clean, you can see yourself "in" them. (does not need to have the quotes around "in"...maybe just italics for this word IN?) You decide for me.

I would like to have a logo designed that incorporates some sort of easy to read letters. I do not want cursive (handwriting) letters. I thought about having a "reflection" of letters (mirror image), but think that this will be hard to read from far away. Maybe you can surprise me and come up with an idea that works using the a mirror image....but I'm not sure. I was leaning toward plain old BLOCK letters as I think it would be easy to read on my truck.

I would like to have the NAQTR and WBK logos on the back of the card. I have attached those two as files. You can put other things on the back as well, but I need these two logos on there. Or maybe put them on the front of the card if you have a better idea for the back of the card! :-)

Maybe blue on the back of the card and white on the front of the card? I don't know, I'm just thinking out loud.

I had another card done awhile ago called HARBORLINE TEES. I have uploaded a copy of that card for your reference. I don't want this card to be the same as my new company is a swimming pool cleaning company, but I wanted you to see what I liked in the past.

THANK YOU!!!!
Updates

Reason: Partner out of town and want their feedback....so need more time to decide and designs still coming in.

Industry/Entity Type

Business

Contact Information for Business Card

GLIMMERTIDE POOL SERVICE
Dale Wexby
Owner
4817 Quarry Bend Ave. #512
San Diego, CA 92417
858-291-6083
www.glimmertidepoolservice.example

Font styles to use
Sans Serif

Colors
0255a3
3176b5
ffffff

Requirements
Nice to have
• Some things to (possibly) add to back of card (in no particular order)
• WBK logo
• NAQTR logo
• Free Estimates
• Residential and Commercial Services
• Equipment Repairs
• Saltwater Systems
• Licensed, Bonded, Insured
• Family Owned and Operated
• No Contracts
• =======================
• Check out the FolioMint business card that i attached.
• i think they did this using a chrome overlay.
• Can any of you guys design that? or is that done at my printer?
• ==================
Should not have
• Hi Designers-
• The first round of cards came back and let's stay away from the light blue (powder blue) color. I don't like the look of it on the business cards.
• Also, the pool company JPG's that I attached are other logos of pool companies that I liked. I don't want them to be on my card. The only logos that should be on my card are the one you are going to come up with for my company, the WBK logo and the NAQTR logo.
• Lastly, no vertical cards and no split cards (logo on left, contact info on right side).
• Thanks much!

```html
<!DOCTYPE html>
<html lang="en">
<head>
<meta charset="utf-8">
<title>Glimmertide Pool Service – Card Back</title>
<link rel="stylesheet" href="https://fonts.googleapis.com/css2?family=Alegreya+Sans+SC:wght@400&family=PT+Sans+Narrow&display=swap">
<style>
  :root {
    --pool-blue: #3176b5;
    --deep-blue: #0255a3;
    --white: #ffffff;
    --badge-fill: #d9e3ee;
  }
  html, body {
    margin: 0;
    padding: 0;
    width: 1200px;
    height: 702px;
    overflow: hidden;
    background: var(--white);
  }
  .card-back {
    position: relative;
    width: 1200px;
    height: 702px;
    background: var(--pool-blue);
    overflow: hidden;
  }
  .wave {
    position: absolute;
    inset: 0;
    width: 1200px;
    height: 702px;
  }
  .badge {
    position: absolute;
    left: 959px;
    width: 176px;
    height: 176px;
    border-radius: 50%;
    background: var(--badge-fill);
  }
  .badge-association { top: 100px; }
  .badge-certification { top: 365px; }
  .service-list {
    position: absolute;
    left: 55px;
    top: 93px;
    margin: 0;
    padding: 0;
    list-style: none;
    font-family: "Alegreya Sans SC", sans-serif;
    font-weight: 400;
    font-size: 32px;
    letter-spacing: 2.2px;
    line-height: 42.6px;
    color: var(--white);
  }
  .service-list li::before {
    content: "- ";
  }
  .website {
    position: absolute;
    left: 76px;
    top: 606px;
    margin: 0;
    font-family: "PT Sans Narrow", sans-serif;
    font-size: 31px;
    line-height: 38px;
    color: var(--white);
  }
</style>
</head>
<body>
  <section class="card-back">
    <svg class="wave" viewBox="0 0 1200 702" aria-hidden="true">
      <path d="M409,0 C560,10 680,70 740,170 C800,270 820,400 880,480 C940,560 1060,620 1200,622 L1200,0 Z" fill="var(--white)"/>
    </svg>

    <div class="badge badge-association" role="img" aria-label="NAQTR association membership badge"></div>
    <div class="badge badge-certification" role="img" aria-label="WBK certified operator badge"></div>

    <ul class="service-list">
      <li>Free Estimates</li>
      <li>Residential and Commercial Services</li>
      <li>Equipment Repairs</li>
      <li>Saltwater Systems</li>
      <li>Licensed, Bonded, Insured</li>
      <li>Family Owned and Operated</li>
      <li>No Contracts</li>
    </ul>

    <p class="website">www.glimmertidepoolservice.example</p>
  </section>
</body>
</html>
```